Landing Page - Mortgage Loan Intake

We are a mortgage company seeking a clean, easy-to-use landing page that consists of minimal copy and creative with a short intake form for customers to sign up to work with us on securing their home financing. We will soon have PX and Google campaigns running throughout the US, and those ads will lead to this landing page. We need at least one landing page for now and may need a slightly different version for A/B testing,. We will expand the project at the beginning of next year with additional versions with the same branding, just geared towards slightly different loan products.

This is the existing intake form we would incorporate on our landing page:

https://apply.quovafin.com/#/create-account

Here is some of the existing content that we would use as a springboard for the design, color scheme, and content of the landing page:

https://brindlehomeloans.com/https://brindlehomeloans.com/about/https://brindlehomeloans.com/refinance/consolidate-debt/

I have also included images that are related to what we're looking for either visually (feel and format) or in terms of the message.

Target Market(s)

people (borrowers) looking for a refinance or debt consolidation through a refinance

Industry/Entity Type

Mortgage Lender

Number of Pages Required

1 page

Font styles to use
Other font styles liked:
• unsure of the name but we would use the font currently used on brindlehomeloans.com

Colors
9bcb3b
cee9f5
ffffff
85acd3
cfeae6
abd036
cadf82
cedeed

Requirements
Must have
• intake form, clean light feel
Nice to have
• explanation of debt consolidation benefits or easy process via a simple infographic or illustration with a clean layout
Should not have
• anything off-brand (colors that are too heavy or not clean and airy)

```html
<!DOCTYPE html>
<html lang="en">
<head>
<meta charset="utf-8">
<title>Consolidate Your Debt – Quovafin by Brindle Home Loans</title>
<link href="https://fonts.googleapis.com/css2?family=Poppins:ital,wght@0,300;0,400;0,500;0,600;0,700;0,800;1,400&display=swap" rel="stylesheet">
<style>
:root{
  --green:#9bcb3b;
  --green-dark:#8cbf2f;
  --blue:#0a74bf;
  --blue-band:rgba(10,116,191,.78);
  --blue-soft:#85acd3;
  --ink:#1b1b1b;
  --text:#555;
  --muted:#8a8a8a;
  --line:#dcdcdc;
  --paper:#ffffff;
  --foot:#f4f4f4;
  --foot-bar:#e6e6e6;
}
*{box-sizing:border-box;margin:0;padding:0}
html,body{width:1200px;height:2917px;overflow:hidden}
body{position:relative;font-family:'Poppins',sans-serif;color:var(--text);background:var(--paper)}
.abs{position:absolute}
.hero{left:0;top:0;width:1200px;height:728px;background:linear-gradient(180deg,#f6f7f6 0%,#eceeec 70%,#e3e5e3 100%)}
.hero-photo{left:80px;top:0;width:560px;height:660px;background:radial-gradient(ellipse at 45% 40%,#5fae3a 0%,#3f8f2a 35%,rgba(120,170,90,.35) 62%,rgba(236,238,236,0) 75%)}
.pot{left:220px;top:470px;width:380px;height:200px;background:linear-gradient(180deg,#f2f2f2,#dcdcdc);border-radius:0 0 30px 30px}
.brand{left:0;width:1200px;top:50px;text-align:center}
.brand-name{font-weight:600;font-size:36px;color:var(--green);letter-spacing:-.5px;line-height:1}
.brand-sub{font-size:9px;color:var(--muted);margin-top:4px}
.hero-band{left:0;top:222px;width:486px;height:284px;background:var(--blue-band)}
.hero-title{left:113px;top:232px;font-weight:800;font-size:56px;line-height:70px;color:#fff}
.hero-lede{left:113px;top:377px;width:330px;font-style:italic;font-size:20px;line-height:27px;color:#fff}
.form-heading{width:602px;text-align:center;font-size:21px;letter-spacing:1px;color:#777;font-weight:300}
.card{width:602px;height:310px;background:#fff;box-shadow:0 2px 10px rgba(0,0,0,.08);border-radius:3px}
.card-foot{position:absolute;left:0;bottom:0;width:100%;height:68px;background:#f4f4f4;border-radius:0 0 3px 3px}
.field{position:absolute;left:29px;width:268px;height:45px;border:1px solid var(--line);border-radius:3px;font-size:13px;color:#9a9a9a;padding-left:42px;line-height:43px;background:#fff}
.field svg{position:absolute;left:15px;top:15px}
.perks{position:absolute;left:327px;top:26px;width:1px;height:230px;background:var(--line)}
.perk{position:absolute;left:354px;width:220px;font-size:10px;line-height:13px;color:#666}
.perk b{display:block;color:#222;font-weight:600;font-size:11px;margin-bottom:2px}
.btn{position:absolute;left:366px;bottom:14px;width:208px;height:40px;background:var(--green);color:#fff;border-radius:2px;font-size:14px;font-weight:500;text-align:center;line-height:40px}
.signin{width:602px;text-align:center;font-size:12px;color:#777}
.signin span{color:#333;text-decoration:underline}
.divider{left:0;top:726px;width:1200px;height:4px;background:var(--blue-soft)}
.scroll-dot{left:573px;top:700px;width:56px;height:56px;border-radius:50%;background:#fff;box-shadow:0 1px 6px rgba(0,0,0,.15)}
.scroll-dot svg{position:absolute;left:18px;top:20px}
.why-title{left:0;top:780px;width:1200px;text-align:center;font-weight:800;font-size:58px;color:var(--ink)}
.house{left:360px;top:930px;width:480px;height:470px;background:radial-gradient(ellipse at 50% 55%,#b9d6ec 0%,#cfe3c0 45%,rgba(255,255,255,0) 72%)}
.benefit{width:300px;text-align:center}
.benefit .ico{width:78px;height:78px;border-radius:50%;margin:0 auto 26px;border:2px solid;display:flex;align-items:center;justify-content:center}
.benefit.green .ico{border-color:var(--green);background:#f3f9e6}
.benefit.blue .ico{border-color:var(--blue-soft);background:#eef4fa}
.benefit.pale .ico{border-color:#cfe0ee;background:#f6f9fc}
.benefit p{font-weight:600;font-size:21px;line-height:28px;color:#333}
.tax{left:0;top:1518px;width:1200px;height:322px;background:linear-gradient(180deg,#0b7bc6,#0867ad)}
.tax h2{position:absolute;left:0;top:76px;width:1200px;text-align:center;font-weight:700;font-size:36px;color:#fff}
.tax p{position:absolute;left:113px;top:140px;width:974px;text-align:center;font-size:15.5px;line-height:24px;color:#d6e8f6}
.when-title{left:113px;top:1962px;width:300px;font-weight:700;font-size:32px;line-height:44px;color:var(--ink)}
.when-copy{left:113px;top:2098px;width:300px;font-size:15.5px;line-height:24px;color:#444}
.footer{left:0;top:2435px;width:1200px;height:427px;background:var(--foot)}
.foot-h{font-size:15px;color:#333;letter-spacing:.3px}
.foot-t{font-size:12.5px;line-height:21px;color:#777}
.foot-brand{font-weight:600;font-size:21px;color:#333}
.badge{width:125px;height:48px;border-radius:4px;background:#1f4f6e}
.foot-bar{left:0;top:2862px;width:1200px;height:55px;background:var(--foot-bar);font-size:10px;color:#555}
</style>
</head>
<body>

<section class="abs hero">
  <div class="abs hero-photo" role="img" aria-label="Photo of a leafy green plant in a white pot"></div>
  <div class="abs pot" role="img" aria-label="White plant pot"></div>
</section>

<header class="abs brand">
  <div class="brand-name">quovafin</div>
  <div class="brand-sub">By Brindle Home Loans</div>
</header>

<div class="abs hero-band"></div>
<h1 class="abs hero-title">Consolidate<br>Your Debt</h1>
<p class="abs hero-lede">The difference between credit card debt and a mortgage can, financially speaking, mean thousands of dollars.</p>

<p class="abs form-heading" style="left:484px;top:156px">Let’s get started on your loan application</p>
<form class="abs card" style="left:484px;top:210px">
  <div class="field" style="top:30px"><svg width="13" height="11" viewBox="0 0 13 11" fill="none" stroke="#888"><rect x=".5" y=".5" width="12" height="10"/><path d="M.5 .5l6 5 6-5"/></svg>Email Address</div>
  <div class="field" style="top:100px"><svg width="13" height="11" viewBox="0 0 13 11" fill="none" stroke="#888"><rect x=".5" y=".5" width="12" height="10"/><path d="M.5 .5l6 5 6-5"/></svg>Confirm email Address</div>
  <div class="field" style="top:170px"><svg width="11" height="13" viewBox="0 0 11 13"><rect y="5" width="11" height="8" fill="#666"/><path d="M2.5 5V3.5a3 3 0 016 0V5" fill="none" stroke="#666" stroke-width="1.5"/></svg>Password</div>
  <div class="perks"></div>
  <div class="perk" style="top:30px"><b>Secure</b>Your data is protected with industry-standard encryption.</div>
  <div class="perk" style="top:108px"><b>Autosaved</b>We’ll save your information as you go.</div>
  <div class="perk" style="top:170px"><b>Less paperwork</b>Import income and asset information directly to your application.</div>
  <div class="card-foot"></div>
  <div class="btn">Create Account</div>
</form>
<p class="abs signin" style="left:484px;top:537px">Already have an account? <span>Sign In</span></p>

<div class="abs divider"></div>
<div class="abs scroll-dot"><svg width="20" height="14" viewBox="0 0 20 14" fill="none" stroke="#85acd3" stroke-width="3"><path d="M2 3l8 8 8-8"/></svg></div>

<h2 class="abs why-title">Why Consolidate?</h2>
<div class="abs house" role="img" aria-label="Infographic of a house shape built from small everyday icons"></div>

<div class="abs benefit green" style="left:75px;top:958px">
  <div class="ico"><svg width="40" height="36" viewBox="0 0 40 36" fill="none" stroke="#9bcb3b" stroke-width="3"><path d="M3 6l12 12 7-7 14 16"/><path d="M26 27h10V17"/></svg></div>
  <p>Lower your interest<br>rates</p>
</div>
<div class="abs benefit green" style="left:75px;top:1164px">
  <div class="ico"><svg width="46" height="28" viewBox="0 0 46 28" fill="none" stroke="#9bcb3b" stroke-width="3"><rect x="2" y="2" width="42" height="24" rx="2"/><circle cx="23" cy="14" r="6"/></svg></div>
  <p>Lower your monthly<br>payments</p>
</div>
<div class="abs benefit blue" style="left:825px;top:958px">
  <div class="ico"><svg width="40" height="40" viewBox="0 0 40 40" fill="none" stroke="#85acd3" stroke-width="3"><circle cx="20" cy="22" r="13"/><path d="M20 14v8l5 4M6 8l6-4M34 8l-6-4"/></svg></div>
  <p>Help you get out of<br>debt faster</p>
</div>
<div class="abs benefit pale" style="left:825px;top:1164px">
  <div class="ico"><svg width="30" height="38" viewBox="0 0 30 38" fill="none" stroke="#a9c6e0" stroke-width="3"><rect x="3" y="16" width="24" height="19" rx="2"/><path d="M8 16v-5a7 7 0 0114 0v5"/></svg></div>
  <p>Protect your credit<br>score</p>
</div>

<section class="abs tax">
  <h2>Mortgage interest is tax-deductible.</h2>
  <p>The interest you pay on a credit card is not tax-deductible and you pay a higher rate than you would on your mortgage. Because of this, credit card debt is often referred to as “bad debt” whereas your mortgage is considered “good debt.” Using your home equity to pay off your high-interest credit card debt can save you money in the long run. Using your home equity, rather than your credit cards, to finance expensive purchases can also be a smart move. Be sure to consult your tax advisor. Trust us on this. Don’t deduct and just cross your fingers for good luck. Know what you are doing before you mess with your taxes!</p>
</section>

<h2 class="abs when-title">When to consolidate your debt.</h2>
<p class="abs when-copy">Deciding on when to refinance your mortgage will depend on the circumstances of your situation: how long you’ll be in the home, what your financial goals are, whether interest rates are dropping, etc. It’s up to you to decide if it’s right for you. In conclusion, your credit scores will soar higher once your credit cards are paid off and you carry low balances.</p>

<p class="abs form-heading" style="left:484px;top:1938px">Let’s get started on your loan application</p>
<form class="abs card" style="left:484px;top:1992px">
  <div class="field" style="top:30px"><svg width="13" height="11" viewBox="0 0 13 11" fill="none" stroke="#888"><rect x=".5" y=".5" width="12" height="10"/><path d="M.5 .5l6 5 6-5"/></svg>Email Address</div>
  <div class="field" style="top:100px"><svg width="13" height="11" viewBox="0 0 13 11" fill="none" stroke="#888"><rect x=".5" y=".5" width="12" height="10"/><path d="M.5 .5l6 5 6-5"/></svg>Confirm email Address</div>
  <div class="field" style="top:170px"><svg width="11" height="13" viewBox="0 0 11 13"><rect y="5" width="11" height="8" fill="#666"/><path d="M2.5 5V3.5a3 3 0 016 0V5" fill="none" stroke="#666" stroke-width="1.5"/></svg>Password</div>
  <div class="perks"></div>
  <div class="perk" style="top:30px"><b>Secure</b>Your data is protected with industry-standard encryption.</div>
  <div class="perk" style="top:108px"><b>Autosaved</b>We’ll save your information as you go.</div>
  <div class="perk" style="top:170px"><b>Less paperwork</b>Import income and asset information directly to your application.</div>
  <div class="card-foot"></div>
  <div class="btn">Create Account</div>
</form>
<p class="abs signin" style="left:484px;top:2318px">Already have an account? <span>Sign In</span></p>

<footer class="abs footer">
  <p class="abs foot-h" style="left:113px;top:50px">BRINDLE HOME LOANS, LLC</p>
  <p class="abs foot-t" style="left:113px;top:90px;width:300px">Brindle is located at:<br>4420 Harbor Crest Blvd. Suite #310<br>Larkspur Bay, CA 90000</p>
  <div class="abs foot-brand" style="left:113px;top:168px">Brindle</div>
  <div class="abs badge" style="left:113px;top:230px" role="img" aria-label="Accreditation badge"></div>
  <div class="abs foot-brand" style="left:113px;top:310px;font-size:18px;color:#1f5f8a">PeerPulse</div>
  <p class="abs foot-h" style="left:612px;top:50px">BRINDLE OPERATES UNDER THE FOLLOWING LICENSES:</p>
  <p class="abs foot-t" style="left:612px;top:85px;width:475px">NMLS ID# 000000 | ALABAMA Lic# 10001 | ARIZONA Lic# 0900001 | CALIFORNIA DBO CFL# 6000001 | CALIFORNIA DRE Lic# 01000001 | COLORADO DRE Lic# LMB1000001 | DC Lic# MLB100001 | FLORIDA Lic# MBR1001 | GEORGIA Lic# 40001 | IDAHO Lic# MBL-1001 | MICHIGAN Lic# FL0010001 | MINNESOTA Lic# MN-MO-100001 | NEBRASKA NDBF | NEW MEXICO RLD | OKLAHOMA Lic# ML010001 | OREGON Lic# ML-1001 | PENNSYLVANIA Lic# 40001 | TEXAS SML Two Willowmere Plaza Suite 200 Fenwick, TX 70000 | UTAH DRE Lic# 9000001 | WASHINGTON Lic# CL-100001</p>
  <p class="abs foot-t" style="left:612px;top:277px;width:475px">To check the licensing under the Nationwide Mortgage Licensing System, visit NMLS Consumer Access;</p>
  <p class="abs foot-t" style="left:612px;top:338px;width:475px">This is not an offer for extension of credit or a commitment to lend. All loans must satisfy company underwriting guidelines.</p>
</footer>

<div class="abs foot-bar">
  <span class="abs" style="left:113px;top:21px">© 2018 Brindle Home Loans, All Rights Reserved. <span style="color:#999">Legal</span></span>
  <span class="abs" style="left:1070px;top:17px;font-size:15px;font-weight:600;color:#444">PX</span>
</div>

</body>
</html>
```